BrambleWorks business card

Looking for business card design that supports our company/software values. We have 2 logo designs at the moment but open to change if you think you can enhance the brand. Check out website www.brambleworks.com.au.

Target Market(s)

Education

Contact Information for Business Card

Name, title, mobile, email and website

Font styles to use
Sans Serif

Colors

Designer to choose colors to be used in the design.

Requirements
Must have
• BrambleWorks logo with tree and tagline on rear side with dark grey background colour

```html
<!DOCTYPE html>
<html lang="en">
<head>
<meta charset="utf-8">
<title>BrambleWorks Business Card</title>
<link href="https://fonts.googleapis.com/css2?family=Open+Sans:wght@400;600&display=swap" rel="stylesheet">
<style>
  :root {
    --backdrop: #5a5a5a;
    --card: #050505;
    --grey-text: #8a8a8a;
    --light-grey: #b0b0b0;
    --green: #4f9a3a;
    --rule-grey: #6a6a6a;
  }
  * { margin: 0; padding: 0; box-sizing: border-box; }
  html, body { width: 1200px; height: 900px; overflow: hidden; }
  body {
    background: linear-gradient(135deg, #3c3c3c 0%, var(--backdrop) 100%);
    font-family: "Open Sans", sans-serif;
    position: relative;
  }
  .card {
    position: absolute;
    left: 280px;
    width: 640px;
    height: 366px;
    background: var(--card);
    box-shadow: 0 10px 28px rgba(0,0,0,0.55);
  }
  .card--front { top: 70px; }
  .card--back { top: 466px; }

  /* Front */
  .front-brand {
    position: absolute;
    left: 0; top: 0;
    width: 330px; height: 366px;
    display: flex; align-items: center; justify-content: center; gap: 12px;
  }
  .brand-dot {
    width: 18px; height: 18px; border-radius: 50%;
    background: var(--green);
  }
  .brand-name {
    font-size: 38px; font-weight: 400;
    color: var(--grey-text);
    letter-spacing: 0.5px;
  }
  .divider {
    position: absolute;
    left: 338px; top: 92px;
    width: 2px; height: 180px;
    background: var(--green);
  }
  .contact {
    position: absolute;
    left: 366px; top: 80px;
  }
  .contact__name {
    font-size: 22px; font-weight: 600;
    color: var(--green);
    line-height: 1.1;
  }
  .contact__title {
    font-size: 14px;
    color: var(--grey-text);
    letter-spacing: 0.5px;
    margin-bottom: 26px;
  }
  .contact__row {
    display: flex; align-items: flex-start; gap: 14px;
    font-size: 13px; color: var(--grey-text);
    margin-bottom: 12px; line-height: 1.3;
  }
  .contact__icon { width: 16px; height: 16px; flex: none; margin-top: 1px; }

  /* Back */
  .back-brand {
    position: absolute;
    left: 0; top: 0; width: 640px; height: 366px;
    display: flex; align-items: center; justify-content: center; gap: 18px;
  }
  .back-brand .brand-dot { width: 26px; height: 26px; }
  .back-lockup { text-align: left; }
  .back-lockup .brand-name {
    font-size: 54px; color: var(--light-grey); display: block;
    padding-bottom: 6px;
    border-bottom: 2px solid var(--rule-grey);
  }
  .tagline {
    display: block;
    font-size: 20px; color: var(--grey-text);
    letter-spacing: 0.6px;
    margin-top: 6px; padding-left: 8px;
  }
</style>
</head>
<body>

<section class="card card--front">
  <div class="front-brand">
    <span class="brand-dot"></span>
    <span class="brand-name">BrambleWorks</span>
  </div>
  <div class="divider"></div>
  <div class="contact">
    <p class="contact__name">NAME HERE</p>
    <p class="contact__title">DESIGNATION</p>
    <div class="contact__row">
      <svg class="contact__icon" viewBox="0 0 24 24"><path fill="#4f9a3a" d="M6.6 10.8a15 15 0 0 0 6.6 6.6l2.2-2.2c.3-.3.7-.4 1-.2 1.1.4 2.3.6 3.6.6.6 0 1 .4 1 1V20c0 .6-.4 1-1 1A17 17 0 0 1 3 4c0-.6.4-1 1-1h3.5c.6 0 1 .4 1 1 0 1.3.2 2.5.6 3.6.1.3 0 .7-.2 1z"/></svg>
      <span>0123 456 789</span>
    </div>
    <div class="contact__row">
      <svg class="contact__icon" viewBox="0 0 24 24"><rect x="2" y="5" width="20" height="14" fill="none" stroke="#4f9a3a" stroke-width="2"/><path d="M2 5l10 8 10-8" fill="none" stroke="#4f9a3a" stroke-width="2"/></svg>
      <span>hello@brambleworks.com</span>
    </div>
    <div class="contact__row">
      <svg class="contact__icon" viewBox="0 0 24 24"><circle cx="12" cy="12" r="9" fill="none" stroke="#4f9a3a" stroke-width="2"/><path d="M3 12h18M12 3c3 3 3 15 0 18M12 3c-3 3-3 15 0 18" fill="none" stroke="#4f9a3a" stroke-width="1.5"/></svg>
      <span>www.brambleworks.com</span>
    </div>
    <div class="contact__row">
      <svg class="contact__icon" viewBox="0 0 24 24"><path fill="#4f9a3a" d="M12 2a7 7 0 0 0-7 7c0 5 7 13 7 13s7-8 7-13a7 7 0 0 0-7-7zm0 9.5A2.5 2.5 0 1 1 12 6.5a2.5 2.5 0 0 1 0 5z"/></svg>
      <span>Address Line 1 Here,<br>Address Line 2 Here</span>
    </div>
  </div>
</section>

<section class="card card--back">
  <div class="back-brand">
    <span class="brand-dot"></span>
    <div class="back-lockup">
      <span class="brand-name">BrambleWorks</span>
      <span class="tagline">Student Success Platform</span>
    </div>
  </div>
</section>

</body>
</html>
```